Thank You Card design for a federal credit union

I am looking to have a thank you card designed.
Specs:
Flat size of 9.5"x6.5" folds to final size of 4.75"x6.5", it will print full color on the front and back. Below, you will see their logo, which needs to print on the inside of the folded card. I also attached images of their current card. They would like to keep the blue color but are open to design on the front. This is a Federal Credit Union, so please make the design, modern and professional. Below is the text that needs to print below the logo on the inside of the card. The text and logo will print below the fold on the inside, leave the top portion (above the panel) white.
Inside text:
Our Members are the foundation of our Credit Union. We sincerely thank you for your loyalty, your business and the opportunity to serve you.
Target Market(s)
Clients of a federal credit union
Industry/Entity Type
Union
Requirements
Must have
- a simple, professional, and modern feel. "Thank You for your business" must be on the front section in some variation.
Should not have
- nothing flashy or too many colors. keep it simple

```html
<!DOCTYPE html>
<html lang="en">
<head>
<meta charset="UTF-8">
<title>Thank You Card – Northline Federal Credit Union</title>
<link href="https://fonts.googleapis.com/css2?family=Great+Vibes&family=Noto+Serif&display=swap" rel="stylesheet">
<style>
  :root {
    --backdrop: #e4e6e7;
    --card-blue: #0a8cc4;
    --card-blue-light: #19a6db;
    --card-blue-deep: #0a6f9f;
    --script-silver: #d9dde0;
    --paper: #ffffff;
    --paper-shade: #f1f2f3;
    --fold-line: #d6d8da;
    --message-blue: #1c67a8;
    --brand-navy: #26296b;
  }
  * { margin: 0; padding: 0; box-sizing: border-box; }
  html, body {
    width: 1200px;
    height: 900px;
    overflow: hidden;
    background: var(--backdrop);
  }
  .canvas {
    position: relative;
    width: 1200px;
    height: 900px;
  }

  /* Front cover */
  .card-front {
    position: absolute;
    left: 80px;
    top: 300px;
    width: 500px;
    height: 340px;
    background: radial-gradient(ellipse at 70% 20%, var(--card-blue-light) 0%, var(--card-blue) 45%, var(--card-blue-deep) 100%);
    box-shadow: 0 6px 18px rgba(0,0,0,0.25);
    overflow: hidden;
  }
  .front-ribbon {
    position: absolute;
    left: 0;
    top: 20px;
    width: 260px;
    height: 160px;
    border-radius: 0 80px 80px 0;
    background: linear-gradient(120deg, rgba(6,90,140,0.45), rgba(40,160,215,0.15));
  }
  .front-greeting {
    position: absolute;
    left: 130px;
    top: 200px;
    font-family: "Great Vibes", cursive;
    font-size: 64px;
    line-height: 1;
    color: var(--script-silver);
    white-space: nowrap;
  }
  .front-subline {
    position: absolute;
    left: 140px;
    top: 272px;
    font-family: "Great Vibes", cursive;
    font-size: 30px;
    color: var(--script-silver);
    white-space: nowrap;
  }

  /* Inside spread */
  .card-inside {
    position: absolute;
    left: 640px;
    top: 90px;
    width: 480px;
    height: 660px;
    background: var(--paper);
    box-shadow: 0 6px 18px rgba(0,0,0,0.25);
  }
  .inside-top {
    height: 330px;
    background: linear-gradient(180deg, var(--paper) 0%, var(--paper-shade) 100%);
    border-bottom: 1px solid var(--fold-line);
  }
  .inside-bottom {
    position: relative;
    height: 330px;
  }
  .inside-message {
    position: absolute;
    left: 30px;
    right: 30px;
    top: 70px;
    font-family: "Noto Serif", serif;
    font-size: 18px;
    line-height: 1.3;
    text-align: center;
    color: var(--message-blue);
  }
  .brand-name {
    position: absolute;
    right: 30px;
    bottom: 60px;
    width: 130px;
    font-family: "Noto Serif", serif;
    font-size: 13px;
    line-height: 1.25;
    text-align: right;
    color: var(--brand-navy);
  }
</style>
</head>
<body>
  <main class="canvas">
    <section class="card-front" aria-label="Card front">
      <div class="front-ribbon" role="img" aria-label="Flowing ribbon swirl ornament in darker blue"></div>
      <p class="front-greeting">Thank You</p>
      <p class="front-subline">for your business</p>
    </section>

    <section class="card-inside" aria-label="Card inside">
      <div class="inside-top"></div>
      <div class="inside-bottom">
        <p class="inside-message">Our Members are the foundation of our Credit Union. We sincerely thank you for your loyalty, your business and the opportunity to serve you.</p>
        <p class="brand-name">Northline Federal Credit Union</p>
      </div>
    </section>
  </main>
</body>
</html>
```